Transportation Brokerage and Freight Forwarder

We need a Facebook company page to attract potential customers (Shippers) and potential Drivers (Truck Drivers) for our business. We provide nationwide shipping services for contract customers in all areas of the Supply Chain LTL (Less than Truck Load), TL (Truck Load) Sea Freight (Ocean Vessels), Air Freight (Air Cargo), Container Freight, Rail Freight (Trains). We are also a Transportation Consulting Company as well helping clients to create Shipping solutions to improve there shipping capacity or cut cost by suggesting different modes of transport based upon their needs.

We have over 50+ years experience in the industry to include Driving (myself and my partner still hold CDL licenses currently), Dispatching Management, Operations Management and former Transport Executives, we are also doing work in other countries with our strategic partners in the form of Freight forwarding services that we offer.

Target Market(s)

The Transport and Shipping community in the U.S., Truck, Train, Ship, Plane & Container

Font styles to use
Serif
Sans Serif

Colors

Designer to choose colors to be used in the design.

Requirements
Must have
• Targeted services we provide (use our website for ideas) www.vrnhtp.com. We want to get the name out there, use stock photos from the Logistics industry
Nice to have
• Appealing attraction to the page itself, want to draw views
Should not have
• No overkill of information

```html
<!DOCTYPE html>
<html lang="en">
<head>
<meta charset="utf-8">
<title>Cargo Bridge Partners Facebook Cover</title>
<link href="https://fonts.googleapis.com/css2?family=Open+Sans:wght@300;400;600&family=Ubuntu:wght@500;700&display=swap" rel="stylesheet">
<style>
  :root {
    --canvas: #5f5f5f;
    --sky: #6abddb;
    --navy: #05316a;
    --ring: #7cc8e4;
    --white: #ffffff;
  }
  html, body {
    margin: 0;
    padding: 0;
    width: 1200px;
    height: 1200px;
    overflow: hidden;
    background: var(--canvas);
  }
  .stage {
    width: 1200px;
    height: 1200px;
    display: flex;
    align-items: center;
    justify-content: center;
  }
  .cover {
    display: block;
    width: 1200px;
    height: 457px;
    box-shadow: 0 2px 6px rgba(0,0,0,0.35);
  }
  .cover__title {
    font-family: "Ubuntu", sans-serif;
    font-weight: 700;
    font-size: 27px;
    fill: var(--white);
  }
  .cover__tagline {
    font-family: "Open Sans", sans-serif;
    font-weight: 300;
    font-size: 17px;
    fill: var(--white);
  }
  .cover__url {
    font-family: "Open Sans", sans-serif;
    font-weight: 400;
    font-size: 14px;
    fill: var(--white);
  }
  .service__label {
    font-family: "Open Sans", sans-serif;
    font-weight: 600;
    font-size: 16.5px;
    fill: var(--white);
  }
</style>
</head>
<body>
<main class="stage">
  <svg class="cover" viewBox="0 0 820 312" xmlns="http://www.w3.org/2000/svg">
    <defs>
      <linearGradient id="sea" x1="0" y1="0" x2="0" y2="1">
        <stop offset="0" stop-color="#b9d3e6"/><stop offset="0.5" stop-color="#e8ecef"/><stop offset="1" stop-color="#4e6f8f"/>
      </linearGradient>
      <linearGradient id="container" x1="0" y1="0" x2="1" y2="1">
        <stop offset="0" stop-color="#3e6e93"/><stop offset="0.5" stop-color="#d86a73"/><stop offset="1" stop-color="#7a5366"/>
      </linearGradient>
      <linearGradient id="truck" x1="0" y1="0" x2="0" y2="1">
        <stop offset="0" stop-color="#c9a57a"/><stop offset="0.5" stop-color="#e9ecef"/><stop offset="1" stop-color="#7d7a6c"/>
      </linearGradient>
      <linearGradient id="train" x1="0" y1="0" x2="1" y2="1">
        <stop offset="0" stop-color="#9fd3ea"/><stop offset="0.45" stop-color="#b8262e"/><stop offset="1" stop-color="#5e6d63"/>
      </linearGradient>
      <linearGradient id="air" x1="0" y1="0" x2="0" y2="1">
        <stop offset="0" stop-color="#52648f"/><stop offset="0.5" stop-color="#d9dee6"/><stop offset="1" stop-color="#3f4f70"/>
      </linearGradient>
    </defs>

    <rect class="cover__sky" width="820" height="312" fill="var(--sky)"/>
    <rect class="cover__band" y="193" width="820" height="119" fill="var(--navy)"/>

    <text class="cover__title" x="426" y="41" text-anchor="middle">CARGO BRIDGE  PARTNERS</text>
    <text class="cover__tagline" x="410" y="65" text-anchor="middle">complete transportation scope</text>

    <g class="cover__url-box">
      <rect x="333.5" y="77.5" width="153" height="26" fill="none" stroke="var(--white)" stroke-width="1"/>
      <circle cx="353" cy="90.5" r="5" fill="none" stroke="var(--white)" stroke-width="0.8"/>
      <ellipse cx="353" cy="90.5" rx="2.2" ry="5" fill="none" stroke="var(--white)" stroke-width="0.6"/>
      <line x1="348" y1="90.5" x2="358" y2="90.5" stroke="var(--white)" stroke-width="0.6"/>
      <text class="cover__url" x="364" y="95.5">www.vrnhtp.com</text>
    </g>

    <g class="service">
      <circle cx="85" cy="187" r="72" fill="var(--ring)"/>
      <circle cx="85" cy="187" r="69" fill="url(#sea)" role="img" aria-label="Photo of a cargo ship loaded with containers"/>
      <text class="service__label" x="85" y="286" text-anchor="middle">Sea Freight</text>
    </g>
    <g class="service">
      <circle cx="249" cy="187" r="72" fill="var(--ring)"/>
      <circle cx="249" cy="187" r="69" fill="url(#container)" role="img" aria-label="Photo of stacked shipping containers and a truck"/>
      <text class="service__label" x="249" y="288" text-anchor="middle">Container Freight</text>
    </g>
    <g class="service">
      <circle cx="411" cy="187" r="72" fill="var(--ring)"/>
      <circle cx="411" cy="187" r="69" fill="url(#truck)" role="img" aria-label="Photo of a semi truck on a desert highway"/>
      <text class="service__label" x="414" y="288" text-anchor="middle">Truck Freight</text>
    </g>
    <g class="service">
      <circle cx="576" cy="187" r="72" fill="var(--ring)"/>
      <circle cx="576" cy="187" r="69" fill="url(#train)" role="img" aria-label="Photo of a freight locomotive"/>
      <text class="service__label" x="579" y="288" text-anchor="middle">Train Freight</text>
    </g>
    <g class="service">
      <circle cx="740" cy="187" r="72" fill="var(--ring)"/>
      <circle cx="740" cy="187" r="69" fill="url(#air)" role="img" aria-label="Photo of a cargo plane at the airport"/>
      <text class="service__label" x="742" y="288" text-anchor="middle">Air Freight</text>
    </g>
  </svg>
</main>
</body>
</html>
```